Optometrist/Eye Care Clinic Business card with new logo attached

We are a small, independent eye care clinic in Canada. We have recently updated our logo (as attached), and would like a professional, modern and health care oriented business card to highlight our office details and our optometrist. We'd like to incorporate the blue colours as seen on our logo.

Target Market(s)

demographic: age 35-65 male/female equal

Industry/Entity Type

Health Care

Contact Information for Business Card

Name of clinic: "Marrow Bend Eye Care Optometry"

Font styles to use
Sans Serif

Colors
0355a3

Requirements
Must have
• our website: marrowbendeyecare.com
• Dr Lena Quorvik
• Optometrist
• 217-392 E Halvering Ave
• Vancouver BC V6R 3J8
• P: 604-319-2058
• E: info@marrowbendeyecare.com
Nice to have
• front side: logo/name of clinic as seen on logo attached and website
• backside: logo on the left side, and name/title/address/phone/email

```html
<!DOCTYPE html>
<html lang="en">
<head>
<meta charset="utf-8">
<title>Marrow Bend Eye Care Optometry – Business Card</title>
<link href="https://fonts.googleapis.com/css2?family=Roboto:wght@400;500;700&display=swap" rel="stylesheet">
<style>
  :root {
    --brand-blue: #0355a3;
    --navy: #1d4f7a;
    --teal: #2a8fb5;
    --ink: #2b2b2b;
    --band-grey: #c4c4c4;
    --card: #ffffff;
    --backdrop: #e9ebee;
  }
  * { box-sizing: border-box; margin: 0; padding: 0; }
  html, body { width: 1200px; height: 800px; overflow: hidden; }
  body {
    background: var(--backdrop);
    font-family: "Roboto", Arial, sans-serif;
    display: flex;
    align-items: center;
    justify-content: center;
    gap: 40px;
  }
  .card {
    position: relative;
    width: 560px;
    height: 320px;
    background: var(--card);
    box-shadow: 0 6px 20px rgba(0,0,0,0.18);
    overflow: hidden;
  }

  /* Clinic name lockup */
  .clinic-name {
    display: flex;
    align-items: center;
    gap: 12px;
    color: var(--navy);
    font-weight: 500;
    text-transform: uppercase;
    letter-spacing: 0.14em;
  }
  .clinic-name .dot {
    flex: none;
    border-radius: 50%;
    background: var(--navy);
  }

  /* Front */
  .card-front {
    display: flex;
    flex-direction: column;
    align-items: center;
    justify-content: center;
  }
  .card-front .clinic-name {
    flex-direction: column;
    gap: 16px;
    font-size: 18px;
    text-align: center;
    line-height: 1.5;
  }
  .card-front .clinic-name .dot { width: 74px; height: 74px; }
  .website {
    margin-top: 26px;
    color: var(--teal);
    font-size: 15px;
  }

  /* Back */
  .card-back .clinic-name {
    position: absolute;
    left: 28px;
    top: 26px;
    font-size: 13px;
    line-height: 1.5;
  }
  .card-back .clinic-name .dot { width: 46px; height: 46px; }
  .divider {
    position: absolute;
    left: 28px;
    right: 0;
    top: 104px;
    height: 1px;
    background: var(--teal);
  }
  .contact {
    position: absolute;
    right: 26px;
    top: 160px;
    text-align: right;
    color: var(--ink);
    font-size: 13px;
    line-height: 1.45;
  }
  .contact .doctor {
    color: var(--brand-blue);
    font-weight: 700;
    font-size: 18px;
    text-transform: uppercase;
    line-height: 1.1;
  }
  .contact .title {
    font-size: 11px;
    text-transform: uppercase;
    letter-spacing: 0.04em;
    margin-bottom: 6px;
  }
  .contact .line-item { display: flex; justify-content: flex-end; align-items: center; gap: 6px; }
  .contact .icon { width: 14px; height: 14px; flex: none; }
  .bands {
    position: absolute;
    left: 0;
    bottom: 0;
    width: 560px;
    height: 28px;
  }
</style>
</head>
<body>

  <section class="card card-front" aria-label="Card front">
    <div class="clinic-name">
      <span class="dot"></span>
      <span>Marrow Bend<br>Eye Care<br>Optometry</span>
    </div>
    <p class="website">www.marrowbendeyecare.com</p>
  </section>

  <section class="card card-back" aria-label="Card back">
    <div class="clinic-name">
      <span class="dot"></span>
      <span>Marrow Bend<br>Eye Care<br>Optometry</span>
    </div>
    <div class="divider"></div>

    <div class="contact">
      <p class="doctor">Dr Lena Quorvik</p>
      <p class="title">Optometrist</p>
      <p>217-392 E Halvering Ave</p>
      <p>Vancouver BC V6R 3J8</p>
      <p class="line-item">604-319-2058
        <svg class="icon" viewBox="0 0 14 14" aria-hidden="true">
          <rect width="14" height="14" fill="#0355a3"/>
          <path d="M4 3 L6 3 L6.6 5 L5.5 6 Q6.5 8 8 8.6 L9 7.5 L11 8 L11 10 Q6 11 3.5 5 Z" fill="#fff"/>
        </svg>
      </p>
      <p class="line-item">info@marrowbendeyecare.com
        <svg class="icon" viewBox="0 0 14 14" aria-hidden="true">
          <rect width="14" height="14" fill="#0355a3"/>
          <rect x="2.5" y="4" width="9" height="6" fill="none" stroke="#fff" stroke-width="1"/>
          <path d="M2.5 4 L7 7.5 L11.5 4" fill="none" stroke="#fff" stroke-width="1"/>
        </svg>
      </p>
    </div>

    <svg class="bands" viewBox="0 0 560 28" preserveAspectRatio="none" aria-hidden="true">
      <polygon points="300,10 560,10 560,28 308,28" fill="#c4c4c4"/>
      <polygon points="0,0 288,14 296,28 0,28" fill="#0355a3"/>
    </svg>
  </section>

</body>
</html>
```